New management consulting website

I need a 4-5 page website that I can manage in WordPress on Hostlane.example for a new management consulting company. The website is www.torvik-example.com and the company name is Torvik Group LLC. The attached spec has an example of a draft site, layout and actual copy and includes company and contact information. I have more high-res images I can send.

Must include instruction/assistance loading the site to my WordPress dashboard.

Target Market(s)

Any business, especially SAAS

Industry/Entity Type

Consultant

Coding

Coded - Design and coding required

Number of Pages Required

4 page

Font styles to use
Sans Serif

Colors
0456a4

Requirements
Must have
• Modern and stylish

```html
<!DOCTYPE html>
<html lang="en">
<head>
<meta charset="utf-8">
<title>Torvik Group LLC — Management Consulting</title>
<link href="https://fonts.googleapis.com/css2?family=Roboto:wght@400;500;700&display=swap" rel="stylesheet">
<style>
:root{
  --brand:#0456a4;
  --navy:#1d4470;
  --ink:#1a1a1a;
  --text:#666;
  --light:#fff;
  --grey:#8d8d8f;
  --footer:#333;
  --footer-line:#4a4a4a;
}
*{margin:0;padding:0;box-sizing:border-box}
html,body{width:1200px;height:3778px;overflow:hidden;background:#fff}
body{font-family:"Roboto",Arial,sans-serif;color:var(--ink);position:relative}
.abs{position:absolute}
a{color:inherit;text-decoration:none}

/* header */
.site-header{left:0;top:0;width:1200px;height:70px;background:#fff;z-index:5}
.brand{left:113px;top:14px;line-height:1}
.brand-name{font-size:32px;font-weight:500;letter-spacing:1px;color:var(--navy)}
.brand-sub{display:block;font-size:10px;letter-spacing:2px;color:var(--grey);margin-top:2px;text-align:center;border-top:1px solid #bbb;padding-top:2px}
.main-nav{left:403px;top:27px;display:flex;gap:29px;font-size:13px;font-weight:500}
.main-nav a.active{color:var(--navy)}
.btn{display:inline-flex;align-items:center;gap:10px;background:var(--navy);color:#fff;font-weight:700;font-size:13px;padding:0 16px;height:48px;border-radius:2px;text-transform:uppercase}
.btn .dot{width:12px;height:12px;border-radius:50%;background:#fff;position:relative}
.btn .dot:after{content:"";position:absolute;left:3px;top:3px;border-left:6px solid var(--navy);border-top:3px solid transparent;border-bottom:3px solid transparent}
.quote-btn{left:936px;top:12px;height:46px}

/* hero */
.hero-photo{left:0;top:70px;width:1200px;height:615px;background:
  radial-gradient(ellipse 420px 300px at 300px 60px,#f6d08a 0%,rgba(214,160,90,.6) 40%,transparent 75%),
  linear-gradient(100deg,#8f7450 0%,#6d6556 35%,#4d5a6a 65%,#2f4a6e 100%)}
.hero-shade{left:0;top:400px;width:1200px;height:285px;background:linear-gradient(180deg,transparent,#2a2a28)}
.hero-title{left:110px;top:244px;font-size:40px;font-weight:700;color:#fff;text-shadow:0 2px 4px rgba(0,0,0,.3)}
.hero-text{left:110px;top:314px;width:580px;font-size:16px;line-height:25px;color:#fff}
.hero-btn{left:110px;top:399px}
.arrow{width:38px;height:38px;border-radius:50%;background:#fff;display:flex;align-items:center;justify-content:center}
.arrow-prev{left:34px;top:330px}
.arrow-next{left:1127px;top:330px}
.hero-wave{left:0;top:485px}

/* about */
.photo{border:4px solid #fff;box-shadow:0 2px 8px rgba(0,0,0,.25)}
.p-meeting{left:111px;top:759px;width:233px;height:187px;background:linear-gradient(135deg,#c7d4df,#7d8f9f 60%,#4d5b67)}
.p-desk{left:360px;top:820px;width:150px;height:120px;background:linear-gradient(135deg,#e9e6e1,#b9c6cf 60%,#8b8f92)}
.p-team{left:192px;top:966px;width:150px;height:119px;background:linear-gradient(135deg,#6f7f91,#a9b5c0 50%,#3e4a58)}
.p-circle{left:360px;top:957px;width:232px;height:186px;background:linear-gradient(135deg,#d6d6d6,#6f6f6f 55%,#2c2c2c)}
.eyebrow{left:675px;top:777px;font-size:14px;font-weight:500}
.section-title{font-size:30px;font-weight:500;color:var(--ink)}
.about-title{left:678px;top:807px}
.rule{width:40px;height:3px;background:var(--navy)}
.about-rule{left:678px;top:857px}
.about-copy{left:675px;top:880px;width:416px;font-size:14px;line-height:25.8px;color:var(--text)}
.about-btn{left:675px;top:1082px}

/* services */
.service{width:318px;height:316px;background:#fff;box-shadow:0 0 6px rgba(0,0,0,.12);padding:36px 23px}
.service-head{display:flex;align-items:flex-start;gap:20px;height:66px}
.service-head h3{font-size:14px;font-weight:700;margin-top:10px}
.service-head .rule{width:28px;height:2px;margin-top:12px}
.service p{font-size:14px;line-height:25.8px;color:var(--text);margin-top:6px}
.more{display:inline-flex;align-items:center;gap:8px;font-size:12px;font-weight:700;color:var(--navy);text-decoration:underline;margin-top:22px}
.more .dot{width:10px;height:10px;border-radius:50%;background:var(--navy)}
.s1{left:0;top:1292px}.s2{left:330px;top:1292px}
.s3{left:0;top:1625px}.s4{left:330px;top:1625px}
.services-panel{left:682px;top:1292px;width:518px;height:650px;background:linear-gradient(180deg,#6f97c9 0%,#4f7db6 55%,#3e6ba8 100%)}
.services-panel-copy{left:742px;top:1503px;width:398px;text-align:center;color:#fff}
.services-panel-copy h2{font-size:21px;font-weight:500}
.services-panel-copy .rule{background:#fff;margin:14px auto 22px;width:32px;height:2px}
.services-panel-copy p{font-size:14px;line-height:25.8px}

/* team */
.team-band{left:0;top:2040px}
.team-photo{left:168px;top:2260px;width:330px;height:330px;border-radius:50%;border:10px solid #fff;background:radial-gradient(circle at 50% 45%,#e3e8ee,#b7c6d8 70%,#9eb3cc);box-shadow:0 2px 10px rgba(0,0,0,.2)}
.team-copy{left:567px;top:2256px;width:520px;color:#fff}
.team-copy h2{font-size:30px;font-weight:500}
.team-copy h3{font-size:21px;font-weight:500;margin-top:16px}
.team-copy h4{font-size:16px;font-weight:700;margin-top:15px}
.team-copy p{font-size:14.5px;line-height:28px;margin-top:12px}
.team-link{display:flex;align-items:center;gap:17px;font-size:15px;margin-top:20px}
.team-link .sq{width:16px;height:16px;border:2px solid #fff;border-radius:3px}

/* origins */
.origins-title{left:0;top:2802px;width:1200px;text-align:center;font-size:28px;font-weight:500}
.origins-copy{left:220px;top:2865px;width:760px;text-align:center;font-size:14.5px;line-height:26px;color:var(--text)}
.scene{top:2968px;height:284px}
.scene-forest{left:111px;width:319px;background:radial-gradient(ellipse at 55% 60%,#9fc24a,#3c6a1f 45%,#1f3a12)}
.scene-sea{left:440px;width:320px;background:linear-gradient(180deg,#2d3b5a 0%,#c46a4a 35%,#f0b04a 45%,#4a7a90 60%,#e8eef0 78%,#8a5a3c 100%)}
.scene-valley{left:769px;width:319px;background:linear-gradient(180deg,#8fb3d4 0%,#b9c5cf 30%,#6f7f62 55%,#3f5a34 80%,#7b8a82 100%)}
.add-btn{left:537px;top:3298px}

/* footer */
.footer-wave{left:0;top:3330px}
.footer-body{left:0;top:3520px;width:1200px;height:258px;background:var(--footer)}
.footer-nav{left:0;top:3535px;width:1200px;display:flex;justify-content:center;gap:26px;color:#fff;font-size:14px;font-weight:700}
.footer-nav span.sep{font-weight:400}
.footer-line{left:111px;top:3598px;width:977px;height:1px;background:var(--footer-line)}
.footer-brand{left:111px;top:3630px;color:#fff;line-height:1}
.footer-brand .brand-name{color:#fff;font-size:44px;font-weight:500}
.footer-brand .brand-sub{color:#fff;font-size:13px;border-color:#fff}
.copyright{left:111px;top:3717px;color:#fff;font-size:14px}
.f-col{color:#fff;font-size:13px}
.f-col h5{font-size:13px;font-weight:700;letter-spacing:.5px;margin-bottom:13px}
.f-row{display:flex;gap:12px;align-items:flex-start;line-height:22px}
.f-office{left:482px;top:3644px}
.f-contact{left:733px;top:3644px}
.phone{font-size:17px;font-weight:500}
.socials{left:948px;top:3646px;display:grid;grid-template-columns:32px 32px;gap:10px}
.socials span{width:32px;height:32px;border:2px solid #fff;border-radius:2px}
</style>
</head>
<body>

<header class="site-header abs">
  <a class="brand abs" href="#"><span class="brand-name">TORVIK</span><span class="brand-sub">CONSULTING</span></a>
  <nav class="main-nav abs">
    <a class="active" href="#">HOME</a><a href="#">ABOUT US</a><a href="#">OUR SERVICES</a><a href="#">OUR TEAM</a><a href="#">CONTACT US</a>
  </nav>
  <a class="btn quote-btn abs" href="#">GET A QUOTE <span class="dot"></span></a>
</header>

<section class="hero">
  <div class="hero-photo abs" role="img" aria-label="Two hikers with raised arms on a mountain summit at sunrise"></div>
  <div class="hero-shade abs"></div>
  <h1 class="hero-title abs">TORVIK GROUP LLC</h1>
  <p class="hero-text abs">Lorem ipsum dolor sit amet, consectetur adipiscing elit, sed do eiusmod tempor incididunt ut labore et dolore magna aliqua.</p>
  <a class="btn hero-btn abs" href="#">GET STARTED <span class="dot"></span></a>
  <span class="arrow arrow-prev abs"><svg width="14" height="14" viewBox="0 0 14 14"><path d="M9 2 L4 7 L9 12" fill="none" stroke="#222" stroke-width="2"/></svg></span>
  <span class="arrow arrow-next abs"><svg width="14" height="14" viewBox="0 0 14 14"><path d="M5 2 L10 7 L5 12" fill="none" stroke="#222" stroke-width="2"/></svg></span>
  <svg class="hero-wave abs" width="1200" height="200" viewBox="0 0 1200 200">
    <path d="M0,90 C90,190 250,200 420,160 C680,100 950,35 1200,55 L1200,80 C950,60 680,120 420,180 C250,215 100,205 0,120 Z" fill="var(--brand)"/>
    <path d="M0,120 C100,205 250,215 420,180 C680,120 950,60 1200,80 L1200,200 L0,200 Z" fill="#fff"/>
  </svg>
</section>

<section class="about">
  <div class="photo p-meeting abs" role="img" aria-label="Team meeting in a glass-walled office"></div>
  <div class="photo p-desk abs" role="img" aria-label="Hands reviewing charts on a tablet"></div>
  <div class="photo p-team abs" role="img" aria-label="Colleagues discussing at a table"></div>
  <div class="photo p-circle abs" role="img" aria-label="Group seated in a circle during a workshop"></div>
  <p class="eyebrow abs">WHO WE ARE</p>
  <h2 class="section-title about-title abs">ABOUT US</h2>
  <div class="rule about-rule abs"></div>
  <p class="about-copy abs">Lorem ipsum dolor sit amet, consectetur adipiscing elit, sed do eiusmod tempor incididunt ut labore et dolore magna aliqua. Ut enim ad minim veniam, quis nostrud exercitation ullamcolaboris nisi ut aliquip ex ea commodo consequat. Duis aute irure dolor in reprehenderit in voluptate velit esse cillum dolore eu fugiat nulla pariatur. Excepteur sint occaecat cupidatat non proident, sunt in culpa qui officia deserunt</p>
  <a class="btn about-btn abs" href="#">LEARN MORE <span class="dot"></span></a>
</section>

<section class="services">
  <article class="service s1 abs">
    <div class="service-head">
      <svg width="36" height="48" viewBox="0 0 36 48"><rect x="3" y="6" width="30" height="40" rx="2" fill="none" stroke="var(--navy)" stroke-width="2.5"/><rect x="11" y="2" width="14" height="7" fill="var(--navy)"/><path d="M9 18l5 5M14 18l-5 5M21 34l5 5M26 34l-5 5M12 36 Q18 24 24 22" fill="none" stroke="var(--brand)" stroke-width="2"/></svg>
      <div><h3>STRATEGY &amp; OPERATIONS</h3><div class="rule"></div></div>
    </div>
    <p>Lorem ipsum dolor sit ameconseadipiscing elit, sed do eiusmod tempor incididunt ut labore et dolore magna aliqua. Ut enim ad minim veniam, quis nostrud exercitation ullamco laboris nisi ut aliquip</p>
    <a class="more" href="#">LEARN MORE <span class="dot"></span></a>
  </article>
  <article class="service s2 abs">
    <div class="service-head">
      <svg width="42" height="46" viewBox="0 0 42 46"><rect x="3" y="30" width="6" height="14" fill="var(--navy)"/><rect x="13" y="22" width="6" height="22" fill="var(--brand)"/><rect x="23" y="26" width="6" height="18" fill="var(--navy)"/><rect x="33" y="14" width="6" height="30" fill="var(--brand)"/><path d="M4 22 L16 12 L26 18 L38 4" fill="none" stroke="var(--navy)" stroke-width="2.5"/></svg>
      <div><h3>DATA ANALYSIS &amp; INSIGHTS</h3><div class="rule"></div></div>
    </div>
    <p>Lorem ipsum dolor sit ameconseadipiscing elit, sed do eiusmod tempor incididunt ut labore et dolore magna aliqua. Ut enim ad minim veniam, quis nostrud exercitation ullamco laboris nisi ut aliquip</p>
    <a class="more" href="#">LEARN MORE <span class="dot"></span></a>
  </article>
  <article class="service s3 abs">
    <div class="service-head">
      <svg width="44" height="48" viewBox="0 0 44 48"><rect x="4" y="20" width="7" height="26" fill="var(--navy)"/><rect x="16" y="4" width="7" height="42" fill="var(--brand)"/><rect x="4" y="10" width="36" height="5" fill="var(--navy)"/><rect x="28" y="36" width="12" height="10" fill="var(--navy)"/></svg>
      <div><h3>LEADERSHIP DEVELOPMENT</h3><div class="rule"></div></div>
    </div>
    <p>Lorem ipsum dolor sit ameconseadipiscing elit, sed do eiusmod tempor incididunt ut labore et dolore magna aliqua. Ut enim ad minim veniam, quis nostrud exercitation ullamco laboris nisi ut aliquip</p>
    <a class="more" href="#">LEARN MORE <span class="dot"></span></a>
  </article>
  <article class="service s4 abs">
    <div class="service-head">
      <svg width="48" height="46" viewBox="0 0 48 46"><rect x="2" y="38" width="14" height="6" fill="var(--navy)"/><rect x="16" y="30" width="14" height="14" fill="var(--brand)"/><rect x="30" y="20" width="14" height="24" fill="var(--navy)"/><path d="M6 30 L18 14 L32 8 L44 2" fill="none" stroke="var(--brand)" stroke-width="2.5"/><circle cx="44" cy="2" r="2" fill="var(--brand)"/></svg>
      <div><h3>EXECUTIVE LEADERSHIP</h3><div class="rule"></div></div>
    </div>
    <p>Lorem ipsum dolor sit ameconseadipiscing elit, sed do eiusmod tempor incididunt ut labore et dolore magna aliqua. Ut enim ad minim veniam, quis nostrud exercitation ullamco laboris nisi ut aliquip</p>
    <a class="more" href="#">LEARN MORE <span class="dot"></span></a>
  </article>
  <div class="services-panel abs" role="img" aria-label="Blue-tinted double exposure of a businessman with a city skyline and flag"></div>
  <div class="services-panel-copy abs">
    <h2>OUR SERVICES</h2>
    <div class="rule"></div>
    <p>Sed ut perspiciatis unde omnis iste natus error sit voluptatem accusantium doloremque laudantium, totam rem aperiam, eaque ipsa quae ab illo inventore veritatis et quasi architecto beatae vitae dicta sunt explicabo.</p>
  </div>
</section>

<section class="team">
  <svg class="team-band abs" width="1200" height="720" viewBox="0 0 1200 720" role="img" aria-label="Blue band with silhouettes of climbers helping each other up a cliff">
    <defs>
      <linearGradient id="teamBlue" x1="0" y1="0" x2="1" y2="0">
        <stop offset="0" stop-color="#3f78be"/><stop offset=".6" stop-color="#2d64ab"/><stop offset="1" stop-color="#0e3d7c"/>
      </linearGradient>
    </defs>
    <path d="M0,100 C300,175 600,80 900,20 C1060,-10 1150,30 1200,90 L1200,560 C1000,520 700,600 420,690 C250,740 60,710 0,640 Z" fill="var(--grey)"/>
    <path d="M0,100 C300,185 600,95 900,40 C1060,12 1150,55 1200,110 L1200,540 C1000,500 700,580 420,670 C250,720 60,690 0,610 Z" fill="url(#teamBlue)"/>
    <path d="M820,660 C900,520 940,380 1000,260 C1060,150 1120,80 1200,110 L1200,540 C1100,530 960,590 820,660 Z" fill="#0b3a75" opacity=".7"/>
  </svg>
  <div class="team-photo abs" role="img" aria-label="Portrait of the founder in a light blue shirt"></div>
  <div class="team-copy abs">
    <h2>OUR TEAM</h2>
    <h3>DANIEL REYES</h3>
    <h4>Founder &amp; Senior Consultant</h4>
    <p>Sed ut perspiciatis unde omnis iste natus error sit voluptatem accusantium doloremque laudantium, totam rem aperiam, eaque ipsa quae ab illinventore veritatis et quasi architecto beatae vitae dicta sunt explicabo. Nemo enim ipsam voluptatem quia voluptas sit aspernatur</p>
    <div class="team-link"><span class="sq"></span>linkedin.com/in/daniel-reyes</div>
  </div>
</section>

<section class="origins">
  <h2 class="origins-title abs">THE ORIGINS OF TORVIK</h2>
  <p class="origins-copy abs">Lorem ipsum dolor sit amet, consectetur adipiscing elit, sed do eiusmod tempor incididunt ut labore et dolore magna aliqua. Ut enim ad minim veniam, quis nostrud exercitation ullamco</p>
  <div class="scene scene-forest abs" role="img" aria-label="Sunlit path through a green forest"></div>
  <div class="scene scene-sea abs" role="img" aria-label="Sunset over waves on a beach"></div>
  <div class="scene scene-valley abs" role="img" aria-label="River valley with pine trees and snowy mountains"></div>
  <a class="btn add-btn abs" href="#">ADD ITEM <span class="dot"></span></a>
</section>

<footer>
  <svg class="footer-wave abs" width="1200" height="200" viewBox="0 0 1200 200">
    <path d="M0,105 C150,170 350,170 550,130 C800,80 1000,0 1200,100 L1200,200 L0,200 Z" fill="var(--brand)"/>
    <path d="M0,118 C150,185 350,185 550,145 C800,95 1020,25 1200,130 L1200,200 L0,200 Z" fill="var(--footer)"/>
  </svg>
  <div class="footer-body abs"></div>
  <nav class="footer-nav abs">
    <a href="#">HOME</a><span class="sep">|</span><a href="#">ABOUT</a><span class="sep">|</span><a href="#">OUR SERVICES</a><span class="sep">|</span><a href="#">CONTACT</a><span class="sep">|</span><a href="#">OUR TEAM</a>
  </nav>
  <div class="footer-line abs"></div>
  <div class="footer-brand abs"><span class="brand-name">TORVIK</span><span class="brand-sub">CONSULTING</span></div>
  <p class="copyright abs">© 2021 Torvik Consulting. All Rights Reserved</p>
  <div class="f-col f-office abs">
    <h5>OFFICE LOCATION</h5>
    <div class="f-row"><svg width="10" height="14" viewBox="0 0 10 14" style="margin-top:4px"><path d="M5 0a5 5 0 0 1 5 5c0 4-5 9-5 9S0 9 0 5a5 5 0 0 1 5-5z" fill="#fff"/><circle cx="5" cy="5" r="2" fill="var(--footer)"/></svg><span>4820 Larkmoor Ave #2100,<br>Brookvale, GA 30999</span></div>
  </div>
  <div class="f-col f-contact abs">
    <h5>CONTACT US</h5>
    <div class="f-row"><svg width="14" height="14" viewBox="0 0 14 14" style="margin-top:4px"><path d="M3 0l3 3-2 2c1 2 3 4 5 5l2-2 3 3-2 3C6 14 0 8 0 3z" fill="#fff"/></svg><span class="phone">555-014-0400</span></div>
    <div class="f-row" style="margin-top:8px"><svg width="14" height="10" viewBox="0 0 14 10" style="margin-top:6px"><rect width="14" height="10" fill="#fff"/><path d="M0 0l7 5 7-5" fill="none" stroke="var(--footer)" stroke-width="1.2"/></svg><span>info@torvik-example.com</span></div>
  </div>
  <div class="socials abs" aria-label="Social links"><span></span><span></span><span></span><span></span></div>
</footer>

</body>
</html>
```